Business Card Design Project

We need a business card for our IT services provider business. We provide services to small and medium business, and would like something that reflects the color scheme / branding on our recently updated website - www.tallobrix.com.au

The card type we have chosen is a matte laminated double sided configuration at 86mm x 54mm on 350 GSM cardboard.
Updates

Target Market(s)

Small and Medium Business owners

Industry/Entity Type

Business

Requirements
Must have
• *Details on all cards*

Company Name: Tallobrix Pty Ltd
ABN: 52 683 914 207
Address: 47-49 Pembury Street, Ashcombe Vale, Victoria 3172
Phone: 1300 GRAB UP
Fax: 03 9417 6258
Website: www.tallobrix.com.au
Logo/Handprint Icon

*Person Specific*

```html
<!DOCTYPE html>
<html lang="en">
<head>
<meta charset="utf-8">
<title>Tallobrix Business Card</title>
<link rel="stylesheet" href="https://fonts.googleapis.com/css2?family=PT+Serif:wght@400;700&display=swap">
<style>
  :root {
    --page-bg: #e4e4e4;
    --brand-blue: #1c66a5;
    --ink-dark: #231f20;
    --icon-dark: #1b1b1b;
    --paper: #ffffff;
    --text-light: #ffffff;
  }
  html, body {
    margin: 0;
    padding: 0;
    width: 1200px;
    height: 1000px;
    overflow: hidden;
    background: var(--page-bg);
    font-family: "PT Serif", Georgia, serif;
  }
  .canvas {
    position: relative;
    width: 1200px;
    height: 1000px;
  }
  .card {
    position: absolute;
    width: 826px;
    height: 462px;
    box-shadow: 0 3px 10px rgba(0,0,0,0.25);
    overflow: hidden;
  }
  .card--front {
    left: 40px;
    top: 27px;
    background: var(--brand-blue);
  }
  .card--back {
    left: 313px;
    top: 513px;
    background: var(--paper);
  }
  .wordmark {
    position: absolute;
    left: 0;
    right: 0;
    text-align: center;
    font-weight: 400;
    letter-spacing: 1px;
    line-height: 1;
  }
  .card--front .wordmark {
    top: 196px;
    font-size: 78px;
    color: var(--text-light);
  }
  .front-website {
    position: absolute;
    left: 0;
    right: 0;
    bottom: 18px;
    text-align: center;
    font-size: 21px;
    color: var(--text-light);
  }
  .back-band {
    position: absolute;
    left: 0;
    top: 0;
    width: 100%;
    height: 256px;
    background: var(--brand-blue);
  }
  .contact-list {
    list-style: none;
    margin: 0;
    padding: 0;
    position: absolute;
    left: 0;
    top: 0;
  }
  .contact-item {
    position: absolute;
    left: 58px;
    display: flex;
    align-items: center;
    gap: 6px;
    font-size: 17px;
    color: var(--text-light);
    white-space: nowrap;
    line-height: 1;
  }
  .contact-icon {
    width: 22px;
    height: 20px;
    flex: none;
  }
  .contact-icon path, .contact-icon rect, .contact-icon circle {
    fill: var(--icon-dark);
  }
  .contact-label {
    color: var(--ink-dark);
  }
  .name-bar {
    position: absolute;
    left: 0;
    top: 266px;
    width: 100%;
    height: 47px;
    background: var(--ink-dark);
    display: flex;
    align-items: center;
  }
  .person-name {
    margin-left: 53px;
    font-size: 26px;
    font-weight: 700;
    color: var(--text-light);
  }
  .person-title {
    margin-left: 46px;
    font-size: 17px;
    color: var(--text-light);
    padding-top: 4px;
  }
  .card--back .wordmark {
    top: 354px;
    font-size: 50px;
    color: var(--ink-dark);
  }
</style>
</head>
<body>
<main class="canvas">

  <section class="card card--front" aria-label="Card front">
    <div class="wordmark">Tallobrix</div>
    <div class="front-website">www.tallobrix.com.au</div>
  </section>

  <section class="card card--back" aria-label="Card back">
    <div class="back-band"></div>

    <ul class="contact-list">
      <li class="contact-item" style="top:40px">
        <svg class="contact-icon" viewBox="0 0 22 20" aria-hidden="true"><path d="M11 1 L1 10 L4 10 L4 19 L9 19 L9 13 L13 13 L13 19 L18 19 L18 10 L21 10 Z"/></svg>
        <span>47-49 Pembury Street, Ashcombe Vale, Victoria 3172</span>
      </li>
      <li class="contact-item" style="top:79px">
        <svg class="contact-icon" viewBox="0 0 22 20" aria-hidden="true"><path d="M1 4 H21 V17 H1 Z M3 6 L11 12 L19 6 Z" fill-rule="evenodd"/></svg>
        <span>firstnamelastname@mailbox.net</span>
      </li>
      <li class="contact-item" style="top:109px">
        <svg class="contact-icon" viewBox="0 0 22 20" aria-hidden="true"><circle cx="11" cy="10" r="9"/><path d="M11 2.5 C7 6 7 14 11 17.5 C15 14 15 6 11 2.5 Z M3 9.3 H19 V10.7 H3 Z" fill="#1c66a5"/></svg>
        <span>www.tallobrix.com.au</span>
      </li>
      <li class="contact-item" style="top:138px">
        <svg class="contact-icon" viewBox="0 0 22 20" aria-hidden="true"><path d="M5 2 L8 2 L10 7 L8 9 C9 11 11 13 13 14 L15 12 L20 14 L20 17 C20 18 19 19 18 19 C10 18 4 12 3 4 C3 3 4 2 5 2 Z"/></svg>
        <span>1300 GRAB UP</span>
      </li>
      <li class="contact-item" style="top:166px">
        <svg class="contact-icon" viewBox="0 0 22 20" aria-hidden="true"><path d="M3 6 H19 V19 H3 Z M6 1 H16 V6 H6 Z"/><rect x="6" y="9" width="6" height="4" fill="#ffffff"/></svg>
        <span>03 9417 6258</span>
      </li>
      <li class="contact-item" style="top:193px">
        <svg class="contact-icon" viewBox="0 0 22 20" aria-hidden="true"><path d="M7 1 H15 V19 H7 Z"/><rect x="8.5" y="3" width="5" height="6" fill="#ffffff"/></svg>
        <span>941 268 3057</span>
      </li>
      <li class="contact-item" style="top:219px; left:56px">
        <span class="contact-label">ABN:</span>
        <span>52 683 914 207</span>
      </li>
    </ul>

    <div class="name-bar">
      <span class="person-name">FirstName LastName</span>
      <span class="person-title">Founder and Mananging Director</span>
    </div>

    <div class="wordmark">Tallobrix</div>
  </section>

</main>
</body>
</html>
```